Business card and Logo for a private personal training studio

We need a business card and logo for a private personal training studio.

The studios name is "Steady Your Path"
Main coloring to be a bright light blue. Looking for a crisp modern look

The front of the card is to have the

Studios name.
The Logo
Private Personal Training Studio
Mel Carver
0451 239 716

The back of the card is to have a lot of words relating to the services we offer. Please place the words vertically and horizontally using different fonts, different text sizes, different boldness and different colors to create a word picture.

Main words that need highlighting are

QVL, PILATES, BOXING, SPIN, STRENGTH, WEIGHT LOSS, BALANCE

Other words to add to the mix with less emphasis

Fitness, Conditioning, Lifestyle, Wellness, Health, Energy, Cardio, Goals, Muscle Tone, Vitality, Confidence, Attitude, Determination, Motivation, Dedication, Fun

Target Market(s)

Woman aged 30 to 60

Industry/Entity Type

Personal Trainer

Contact Information for Business Card

Steady Your Path
Mel Carver
0451 239 716

Colors
0493ce
33a6d7
85cae6

```html
<!DOCTYPE html>
<html lang="en">
<head>
<meta charset="utf-8">
<title>Steady Your Path – Business Card</title>
<link href="https://fonts.googleapis.com/css2?family=Questrial&family=Open+Sans:wght@400;600;700;800&display=swap" rel="stylesheet">
<style>
  :root {
    --blue-deep: #0493ce;
    --blue-mid: #33a6d7;
    --blue-light: #85cae6;
    --blue-ink: #1f6fa6;
    --grey-text: #8a8a8a;
    --grey-dark: #6f6f6f;
    --grey-bold: #a3a3a3;
    --card: #ffffff;
    --backdrop: #e9edf0;
  }
  * { margin: 0; padding: 0; box-sizing: border-box; }
  html, body { width: 1200px; height: 1062px; overflow: hidden; }
  body {
    background: var(--backdrop);
    font-family: "Open Sans", sans-serif;
    position: relative;
  }
  .card {
    position: absolute;
    left: 250px;
    width: 700px;
    height: 400px;
    background: var(--card);
    box-shadow: 0 6px 22px rgba(0,0,0,0.12);
    overflow: hidden;
  }
  .card--front { top: 90px; }
  .card--back { top: 572px; }

  /* Front */
  .brand { position: absolute; left: 60px; top: 120px; display: flex; align-items: center; gap: 22px; }
  .brand__dot { width: 58px; height: 58px; border-radius: 50%; background: var(--blue-light); flex: none; }
  .brand__name { font-family: "Questrial", sans-serif; font-size: 54px; font-weight: 400; color: var(--blue-mid); line-height: 1; }
  .brand__tagline { position: absolute; left: 141px; top: 184px; font-family: "Questrial", sans-serif; font-size: 22px; letter-spacing: 1.5px; color: var(--grey-text); }
  .contact { position: absolute; left: 141px; top: 250px; font-size: 15px; color: var(--grey-dark); line-height: 1.9; }
  .contact__person { font-weight: 600; color: var(--blue-mid); font-size: 17px; }
  .contact__sep { color: var(--grey-dark); margin: 0 8px; }
  .contact__row { display: flex; align-items: center; gap: 8px; }
  .contact__icon { width: 14px; height: 14px; flex: none; }
  .contact__at { color: var(--blue-mid); font-weight: 600; width: 14px; text-align: center; }

  /* Back word picture */
  .cloud {
    position: absolute;
    left: 26px;
    top: 18px;
    width: 600px;
    height: 364px;
    display: flex;
    flex-direction: column;
    justify-content: space-between;
  }
  .cloud__row { display: flex; align-items: baseline; gap: 16px; white-space: nowrap; }
  .word { line-height: 1; white-space: nowrap; }

  .w-goals, .w-lifestyle, .w-attitude { font-size: 20px; font-weight: 600; color: var(--grey-dark); }
  .w-health { font-size: 22px; font-weight: 700; color: var(--blue-mid); }
  .w-fun { font-size: 20px; font-weight: 700; color: var(--blue-mid); }
  .w-fitness { font-size: 21px; font-weight: 400; color: var(--grey-text); }

  .w-muscletone { font-size: 20px; font-weight: 600; color: var(--grey-dark); }
  .w-vitality { font-size: 26px; font-weight: 600; color: var(--blue-mid); }
  .w-qvl { font-size: 76px; font-weight: 800; color: var(--blue-mid); }

  .w-spin { font-size: 40px; font-weight: 800; color: var(--blue-ink); }
  .w-energy { font-size: 34px; font-weight: 700; color: var(--blue-mid); }
  .w-pilates { font-size: 40px; font-weight: 800; color: var(--blue-mid); }

  .w-balance { font-size: 44px; font-weight: 800; color: var(--blue-mid); }
  .w-boxing { font-size: 40px; font-weight: 800; color: var(--blue-deep); }

  .w-weightloss { font-size: 54px; font-weight: 800; color: var(--blue-deep); }
  .w-dedication { font-size: 26px; font-weight: 400; color: var(--grey-dark); }

  .w-strength { font-size: 36px; font-weight: 800; color: var(--grey-bold); }
  .w-motivation { font-size: 32px; font-weight: 700; color: var(--blue-mid); }
  .w-confidence { font-size: 20px; font-weight: 600; color: var(--grey-dark); }

  .w-conditioning { font-family: "Questrial", sans-serif; font-size: 18px; letter-spacing: 5px; color: var(--grey-text); }
  .w-wellness { font-size: 15px; color: var(--grey-text); }
  .w-cardio { font-size: 22px; font-weight: 600; color: var(--blue-mid); }

  .w-determination {
    position: absolute;
    right: 26px;
    top: 60px;
    writing-mode: vertical-rl;
    font-family: "Questrial", sans-serif;
    font-size: 20px;
    letter-spacing: 6px;
    color: var(--grey-text);
  }
</style>
</head>
<body>

<section class="card card--front" aria-label="Card front">
  <div class="brand">
    <span class="brand__dot"></span>
    <h1 class="brand__name">Steady Your Path</h1>
  </div>
  <p class="brand__tagline">Private Personal Training Studio</p>
  <div class="contact">
    <p><span class="contact__person">Mel Carver</span><span class="contact__sep">•</span>Manager</p>
    <p class="contact__row">
      <svg class="contact__icon" viewBox="0 0 24 24" aria-hidden="true"><path d="M6.6 10.8a15 15 0 0 0 6.6 6.6l2.2-2.2c.3-.3.7-.4 1-.2 1.1.4 2.3.6 3.6.6.6 0 1 .4 1 1V20c0 .6-.4 1-1 1A17 17 0 0 1 3 4c0-.6.4-1 1-1h3.5c.6 0 1 .4 1 1 0 1.3.2 2.5.6 3.6.1.3 0 .7-.2 1z" fill="#33a6d7"/></svg>
      0451 239 716
    </p>
    <p class="contact__row">
      <svg class="contact__icon" viewBox="0 0 24 24" aria-hidden="true"><g fill="none" stroke="#33a6d7" stroke-width="2"><circle cx="12" cy="12" r="9"/><ellipse cx="12" cy="12" rx="4" ry="9"/><line x1="3" y1="12" x2="21" y2="12"/></g></svg>
      www.steadypathstudio.com
    </p>
    <p class="contact__row"><span class="contact__at">@</span>hello@steadypathstudio.com</p>
  </div>
</section>

<section class="card card--back" aria-label="Card back word picture">
  <div class="cloud">
    <div class="cloud__row">
      <span class="word w-goals">Goals</span>
      <span class="word w-lifestyle">Lifestyle</span>
      <span class="word w-attitude">Attitude</span>
      <span class="word w-health">Health</span>
      <span class="word w-fun">Fun</span>
      <span class="word w-fitness">Fitness</span>
    </div>
    <div class="cloud__row">
      <span class="word w-muscletone">Muscle Tone</span>
      <span class="word w-vitality">Vitality</span>
      <span class="word w-qvl">QVL</span>
    </div>
    <div class="cloud__row">
      <span class="word w-spin">SPIN</span>
      <span class="word w-energy">Energy</span>
      <span class="word w-pilates">PILATES</span>
    </div>
    <div class="cloud__row">
      <span class="word w-balance">BALANCE</span>
      <span class="word w-boxing">BOXING</span>
    </div>
    <div class="cloud__row">
      <span class="word w-weightloss">WEIGHT LOSS</span>
      <span class="word w-dedication">Dedication</span>
    </div>
    <div class="cloud__row">
      <span class="word w-strength">STRENGTH</span>
      <span class="word w-motivation">Motivation</span>
      <span class="word w-confidence">Confidence</span>
    </div>
    <div class="cloud__row">
      <span class="word w-conditioning">Conditioning</span>
      <span class="word w-wellness">Wellness</span>
      <span class="word w-cardio">Cardio</span>
    </div>
  </div>
  <span class="word w-determination">Determination</span>
</section>

</body>
</html>
```